StoneBay construction business cards

I need a business card with a replacement window photo or graphic on it .phone # 919 482 -7316 stonebayconstruction@mailfort.net fax #919 274-8093 '' The Window Replacement Specialist"

Industry/Entity Type

Construction

```html
<!DOCTYPE html>
<html lang="en">
<head>
<meta charset="utf-8">
<title>StoneBay Construction – Business Cards</title>
<link href="https://fonts.googleapis.com/css2?family=Roboto:wght@400;700&display=swap" rel="stylesheet">
<style>
  :root {
    --page-bg: #e9e7e4;
    --card-white: #ffffff;
    --band-brown: #2a1913;
    --brand-green: #6cc04a;
    --photo-dark: #1e1614;
    --photo-mid: #3a2c26;
    --text-light: #f4f1ee;
    --tagline-grey: #4a4a4a;
  }
  * { box-sizing: border-box; margin: 0; padding: 0; }
  html, body {
    width: 1200px; height: 1000px; overflow: hidden;
    background: var(--page-bg);
    font-family: "Roboto", Arial, sans-serif;
  }
  .card {
    position: absolute; left: 300px;
    width: 600px; height: 343px;
    border-radius: 4px;
    box-shadow: 0 6px 18px rgba(0,0,0,0.18);
    overflow: hidden;
  }
  .card-front { top: 100px; background: var(--photo-dark); }
  .card-back  { top: 557px; background: var(--card-white); }

  .window-photo {
    position: absolute; inset: 0;
    background:
      radial-gradient(ellipse at 50% 30%, rgba(110,95,80,0.35), transparent 65%),
      linear-gradient(180deg, var(--photo-mid) 0%, var(--photo-dark) 100%);
  }
  .brand-name {
    position: absolute; left: 0; right: 0;
    text-align: center; font-weight: 700;
    letter-spacing: 1px;
  }
  .card-front .brand-name {
    top: 140px; font-size: 38px; color: var(--text-light);
  }
  .card-back .brand-name {
    top: 62px; font-size: 28px; color: var(--brand-green);
  }
  .contact-band { position: absolute; left: 0; top: 118px; width: 600px; height: 90px; }
  .contact {
    position: absolute; top: 170px;
    display: flex; align-items: center; gap: 6px;
    font-size: 12px; color: var(--text-light);
  }
  .contact svg { width: 11px; height: 11px; }
  .contact-phone { left: 24px; }
  .contact-email { left: 200px; }
  .contact-fax { right: 24px; }
  .tagline {
    position: absolute; left: 0; right: 0; top: 262px;
    text-align: center; font-size: 10px; font-weight: 700;
    letter-spacing: 3px; color: var(--tagline-grey);
  }
</style>
</head>
<body>
  <section class="card card-front">
    <div class="window-photo" role="img" aria-label="Photo of a living room with large replacement windows, darkened"></div>
    <div class="brand-name">StoneBay Construction</div>
  </section>

  <section class="card card-back">
    <div class="brand-name">StoneBay Construction</div>
    <svg class="contact-band" viewBox="0 0 600 90" aria-hidden="true">
      <polygon points="0,30 285,30 300,18 315,30 600,30 600,80 0,80" fill="var(--band-brown)"/>
    </svg>
    <div class="contact contact-phone">
      <svg viewBox="0 0 12 12"><path d="M3 1l2 2-1 1.5a6 6 0 0 0 3.5 3.5L9 7l2 2-1.5 2C5 11 1 7 1 2.5z" fill="var(--brand-green)"/></svg>
      919 482 -7316
    </div>
    <div class="contact contact-email">
      <svg viewBox="0 0 12 12"><rect x="1" y="2.5" width="10" height="7" fill="none" stroke="var(--brand-green)"/><path d="M1 2.5l5 4 5-4" fill="none" stroke="var(--brand-green)"/></svg>
      stonebayconstruction@mailfort.net
    </div>
    <div class="contact contact-fax">
      <svg viewBox="0 0 12 12"><rect x="3" y="1" width="6" height="4" fill="none" stroke="var(--brand-green)"/><rect x="1" y="5" width="10" height="6" fill="var(--brand-green)"/></svg>
      919 274-8093
    </div>
    <div class="tagline">THE WINDOW REPLACEMENT SPECIALIST</div>
  </section>
</body>
</html>
```